webdesign for a spectacles/glasses designer

Hello,

Someone in my village designs his own spectacles/eyeglasses.

For this I need a design that looks better than my poor design skills ;o)

The site is based around collections, subcollections and the actual items.

So we need a design that lists these in a nice way, worst case on seperate pages.

Here you can find the working material...

https://www.filevaultic.com/s/q7kmtr4p2wz91xb/BriefHarbor.zip

keep an eye on the product_tree file.

first level is the collection name
2nd is the model group
3rd is the model (on most of them it's just a different color of the same base model)

I added a seperate contact info file (line is too slow to reupload 60Mb again :( )

https://dl.filevaulticcontent.com/u/31906524/Anselm/contact.zip

I think I forgot to mention that it will be a shop like site to present his products,
altho I will add a cart system there won't be a payment system linked to it as
people who place orders will get contacted with payment instructions.
Updates

In the zipfile /Logo/logo_mistral_font.psd is the main logo
(you need to change character spacing to 1 to get rid of the spacing gaps)

the other one is only a collection logo

Target Market(s)

Plain customers and his resellers.

Industry/Entity Type

Shop

Requirements
Must have
• - a design that suits responsive behaviour (via the 960 grid)
- a menu is always handy (home, about, collections, contact)
- highlighted area/slider to highlight his sunglasses over glasses thingy
- featured products (newly added or promotional stuff)

there is a lot of pretty pictures to be supplied so do what you think is best

Nice to have
• a roll over zoom with selectable thumbnails or a plain gallery with full picture display at the product page.

maybe a drop down menu for the collection part (I will supply a screenshot of the backend structure)

```html
<!DOCTYPE html>
<html lang="en">
<head>
<meta charset="utf-8">
<title>Anselm — Eyewear</title>
<link rel="stylesheet" href="https://fonts.googleapis.com/css2?family=Didact+Gothic&family=Arimo:wght@400;700&family=Open+Sans:wght@400&display=swap">
<style>
:root{
  --red:#d40f0f;
  --ink:#1a1a1a;
  --text:#555;
  --rule:#d6d6d6;
  --footer:#2f2f2f;
  --footer-base:#222;
  --footer-text:#e6e6e6;
  --teal:#5cb3b8;
  --orange:#f5a313;
  --nav:#222;
}
*{margin:0;padding:0;box-sizing:border-box}
html,body{width:935px;height:1200px;overflow:hidden;background:#fff}
body{position:relative;font-family:"Arimo",Arial,sans-serif;color:var(--ink)}

.site-header{position:absolute;left:0;top:0;width:935px;height:94px;background:linear-gradient(#fff,#f1f1f1)}
.brand{position:absolute;left:74px;top:18px;font-family:"Didact Gothic",sans-serif;font-size:50px;line-height:60px;color:#111;letter-spacing:1px}
.phone{position:absolute;left:631px;top:8px;display:flex;align-items:center;gap:8px;font-family:"Didact Gothic",sans-serif;font-size:19px;letter-spacing:.9px;color:#222;line-height:20px}
.phone-badge{width:20px;height:20px;border-radius:3px;background:var(--red);display:flex;align-items:center;justify-content:center}
.main-nav{position:absolute;left:0;top:0;width:935px;height:94px;font-family:"Didact Gothic",sans-serif;font-size:15px;letter-spacing:.4px;color:var(--nav)}
.nav-item,.nav-sep{position:absolute;top:67px;line-height:18px;color:var(--nav)}
.nav-underline{position:absolute;left:474px;top:90px;width:57px;height:3px;background:var(--red)}

.hero{position:absolute;left:0;top:94px;width:935px;height:387px;background:radial-gradient(ellipse at 55% 45%,#c9a78f 0%,#a9908a 28%,#8a8684 55%,#858585 100%);box-shadow:0 4px 8px rgba(0,0,0,.15)}
.hero-arrow{position:absolute;top:179px;width:29px;height:29px;border:2.5px solid rgba(255,255,255,.8);border-radius:50%}
.hero-dots{position:absolute;top:363px;left:417px;display:flex;align-items:center;gap:5px}
.hero-dots span{width:8px;height:8px;border:1.5px solid #fff;border-radius:50%}
.hero-dots span.on{background:#fff}
.hero-dots span.ctl{width:15px;height:15px;border-width:2px}

.section-title{position:absolute;left:92px;width:757px;text-align:center;font-family:"Didact Gothic",sans-serif;font-weight:400;color:#111;line-height:1}
.section-title .small{display:block;font-size:16px;letter-spacing:.5px}
.section-title .big{display:block;font-size:27px;letter-spacing:1px}
.section-title::before,.section-title::after{content:"";position:absolute;left:0;right:0;border-top:1px solid var(--rule)}
.section-title::before{top:11px}
.section-title::after{top:27px}
.section-title .mask{position:relative;z-index:1;background:#fff;display:inline-block;padding:0 12px}

.service{position:absolute;top:578px;width:240px;text-align:center}
.service-icon{width:30px;height:30px;border-radius:50%;margin:0 auto 20px;display:flex;align-items:center;justify-content:center}
.service h3{font-family:"Didact Gothic",sans-serif;font-weight:400;font-size:19px;color:#222;margin-bottom:3px}
.service p{font-size:9.6px;line-height:13.5px;color:var(--text)}
.service .more{display:block;margin-top:10px;font-size:10px;color:var(--red);text-decoration:none}

.product{position:absolute;top:806px;width:190px;text-align:center}
.product-photo{width:148px;height:148px;margin:0 auto;border-radius:50%;border:6px solid #efefef;box-shadow:0 10px 8px -6px rgba(0,0,0,.35)}
.product .code{margin-top:22px;font-weight:700;font-size:10.5px;letter-spacing:.5px}
.product .name{font-size:11px;letter-spacing:.3px;margin-top:2px}
.product .finish{font-size:11px;color:var(--red);letter-spacing:.3px;margin-top:1px}

.site-footer{position:absolute;left:0;top:1054px;width:935px;height:114px;background:var(--footer);font-family:"Open Sans",sans-serif;color:var(--footer-text)}
.footer-col{position:absolute;top:20px}
.footer-col h4{font-family:"Didact Gothic",sans-serif;font-weight:400;font-size:15px;letter-spacing:.6px;margin-bottom:8px}
.footer-col ul{list-style:none;font-size:11px;line-height:19px;letter-spacing:.5px}
.footer-col li::before{content:"●";font-size:7px;margin-right:9px;vertical-align:2px}
.signup{position:absolute;left:652px;top:44px;display:flex;gap:4px}
.signup .field{width:105px;height:18px;background:#fff;border:1px solid #bbb;font-size:9.5px;color:#999;padding:2px 4px}
.signup .btn{width:55px;height:18px;background:#000;color:#fff;font-family:"Arimo",sans-serif;font-weight:700;font-size:10px;display:flex;align-items:center;justify-content:center}
.social{position:absolute;left:653px;top:81px;display:flex;gap:11px}
.social span{width:20px;height:20px;border-radius:50%;background:#fff}
.footer-base{position:absolute;left:0;top:1168px;width:935px;height:32px;background:var(--footer-base);color:#ddd;font-family:"Open Sans",sans-serif;font-size:10.5px;text-align:center;line-height:32px}
</style>
</head>
<body>

<header class="site-header">
  <div class="brand">Anselm</div>
  <div class="phone">
    <span class="phone-badge"><svg width="12" height="12" viewBox="0 0 24 24"><path fill="#fff" d="M6.6 10.8c1.4 2.8 3.8 5.1 6.6 6.6l2.2-2.2c.3-.3.7-.4 1-.2 1.1.4 2.3.6 3.6.6.6 0 1 .4 1 1V20c0 .6-.4 1-1 1C10.6 21 3 13.4 3 4c0-.6.4-1 1-1h3.5c.6 0 1 .4 1 1 0 1.3.2 2.5.6 3.6.1.3 0 .7-.2 1z"/></svg></span>
    <span>tel.: +32(0)51.48.26.19</span>
  </div>
  <nav class="main-nav">
    <span class="nav-item" style="left:482px">Home</span>
    <span class="nav-sep" style="left:548px">|</span>
    <span class="nav-item" style="left:580px">About</span>
    <span class="nav-sep" style="left:648px">|</span>
    <span class="nav-item" style="left:679px">Collections</span>
    <span class="nav-sep" style="left:780px">|</span>
    <span class="nav-item" style="left:813px">Contact</span>
    <span class="nav-underline"></span>
  </nav>
</header>

<section class="hero" role="img" aria-label="Slider photo of a model adjusting dark overlay sunglasses">
  <span class="hero-arrow" style="left:7px"></span>
  <span class="hero-arrow" style="left:898px"></span>
  <div class="hero-dots">
    <span class="ctl"></span><span></span><span></span><span class="on"></span><span></span><span></span><span class="ctl"></span>
  </div>
</section>

<h2 class="section-title" style="top:514px"><span class="mask"><span class="small">OUR</span><span class="big">Services</span></span></h2>

<div class="service" style="left:74px">
  <div class="service-icon" style="background:var(--teal)"><svg width="16" height="16" viewBox="0 0 16 16" fill="none" stroke="#fff" stroke-width="1.3"><rect x="2.5" y="6" width="11" height="8"/><rect x="1.5" y="4" width="13" height="2.5"/><path d="M8 4v10M2.5 10h11"/></svg></div>
  <h3>Free shipping...fast!</h3>
  <p>We offer free shipping on all domestic orders, with no minimums or exceptions. Your order will arrive on your doorstep within 7-10 business days.</p>
  <a class="more">Learn more</a>
</div>
<div class="service" style="left:350px">
  <div class="service-icon" style="background:var(--red)"><svg width="18" height="18" viewBox="0 0 18 18" fill="none" stroke="#fff" stroke-width="2"><path d="M3.5 8a5.5 5.5 0 0 1 10-2.5M14.5 10a5.5 5.5 0 0 1-10 2.5"/><path d="M14 2.5v3.5h-3.5M4 15.5V12h3.5"/></svg></div>
  <h3>Free 90-day returns.</h3>
  <p>We offer a no hassle, 90-day return policy from the day we ship your order. We'll even pick up the tab for return shipping so you can shop risk-free.</p>
  <a class="more">Learn more</a>
</div>
<div class="service" style="left:624px">
  <div class="service-icon" style="background:var(--orange)"><svg width="16" height="16" viewBox="0 0 16 16"><circle cx="8" cy="8" r="4" fill="#fff"/><g stroke="#fff" stroke-width="1.4"><path d="M8 1v3M8 12v3M1 8h3M12 8h3M3 3l2 2M11 11l2 2M13 3l-2 2M5 11l-2 2"/></g></svg></div>
  <h3>2-Year Warranty.</h3>
  <p>We offer a 2-year warranty that covers everything from scratches to you sitting on them in your car. If we are unable to repair your glasses, you get a free pair.</p>
  <a class="more">Learn more</a>
</div>

<h2 class="section-title" style="top:749px"><span class="mask"><span class="small">BEST</span><span class="big">Selling</span></span></h2>

<div class="product" style="left:68px">
  <div class="product-photo" role="img" aria-label="Model lifting red framed overlay sunglasses" style="background:radial-gradient(circle at 50% 45%,#b89a84,#7d7b7a 70%)"></div>
  <div class="code">ANS02</div><div class="name">Stylish overlay sunglasses</div><div class="finish">Red framed</div>
</div>
<div class="product" style="left:278px">
  <div class="product-photo" role="img" aria-label="Model wearing purple and red glasses" style="background:radial-gradient(circle at 50% 45%,#c4a88e,#858382 70%)"></div>
  <div class="code">AN25-Col03</div><div class="name">Classy Glasses</div><div class="finish">Purple/red framed</div>
</div>
<div class="product" style="left:484px">
  <div class="product-photo" role="img" aria-label="Model wearing black overlay sunglasses" style="background:radial-gradient(circle at 50% 45%,#b8977d,#7e7b79 70%)"></div>
  <div class="code">ANS02</div><div class="name">Stylish overlay sunglasses</div><div class="finish">Black frames</div>
</div>
<div class="product" style="left:673px">
  <div class="product-photo" role="img" aria-label="Orange and red framed glasses on white" style="background:radial-gradient(circle at 50% 50%,#f7e2d2,#f4f4f4 60%)"></div>
  <div class="code">AN22-Col03</div><div class="name">Extra contoured glasses</div><div class="finish">Orange/red framed</div>
</div>

<footer class="site-footer">
  <div class="footer-col" style="left:83px"><h4>Best sellers</h4><ul><li>Woman</li><li>Men</li></ul></div>
  <div class="footer-col" style="left:222px"><h4>Eye glasses</h4><ul><li>Woman</li><li>Men</li></ul></div>
  <div class="footer-col" style="left:369px"><h4>Sunglasses</h4><ul><li>Woman</li><li>Men</li></ul></div>
  <div class="footer-col" style="left:512px"><h4>Newletter</h4><ul><li>Woman</li><li>Men</li></ul></div>
  <div class="footer-col" style="left:652px"><h4>Dont miss out!</h4></div>
  <div class="signup"><div class="field">enter your email</div><div class="btn">Sign up</div></div>
  <div class="social"><span></span><span></span><span></span><span></span><span></span></div>
</footer>
<div class="footer-base">anselm © copyright 2013 | privacy policy</div>

</body>
</html>
```